Zielgruppe
Wir sind ein junges Unternehmen im Bereich der Werbemittelbranche. Wir vertreiben u.a. Seccodosen im individuellen Design nach Kundenwunsch nur an B2B. Wir möchten eine Secco Dose entwickeln lassen, die
- als Eigenwerbung dienen soll (Abgabe an potentielle B2B Kunden ) und
- als Secco im Handel (Kioske, Touristshops B2C )
genutzt / verkauft werden kann.
Dies vor dem Hintergrund von möglichen sportlichen Großereignissen in Köln
(weitere Zielgruppenspezifische Ideen in Planung)
Aufgabenstellung
Entwicklung eines Dosenetiketts (PE-Kunststoffetikett) für eine 200 ML Secco Dose. Inhalt orginal italienischer IGT Secco Bianco.
Pflichttexte und Druckvorgaben/Stanze für Etikett wird geliefert.
Name: RheinPerlwein
Markantes plakatives Design.
Ggf. Nutzung der Kölner Signalfarben rot - schwarz- weiss
Hinweis zur Gestaltung - Optik.
Dosenmaterial Aluminium.
Es gibt 2 Optionen, die für die Gestaltung /Optik interessant sind:
1. Druck auf transparenter Folie. Optischer Eindruck wie ein Direktdruck auf Dose.
2. 1-4 C Druck auf weißer Folie

```html
<!DOCTYPE html>
<html lang="de">
<head>
<meta charset="utf-8">
<title>RheinPerlwein – Dosenetikett 200 ml</title>
<link rel="stylesheet" href="https://fonts.googleapis.com/css2?family=Open+Sans:wght@400;600;700&display=swap">
<style>
  :root {
    --stage: #f4f4f4;
    --label: #ffffff;
    --label-edge: #d9d9d9;
    --signal-red: #e30613;
    --skyline-tint: #f9d3d5;
    --ink: #1a1a1a;
    --ink-soft: #3a3a3a;
  }
  * { box-sizing: border-box; margin: 0; padding: 0; }
  html, body {
    width: 1200px; height: 900px; overflow: hidden;
    background: var(--stage);
    font-family: "Open Sans", Arial, sans-serif;
  }
  .can-label {
    position: absolute;
    left: 60px; top: 140px;
    width: 1080px; height: 620px;
    background: var(--label);
    border-right: 10px solid var(--label-edge);
    box-shadow: 0 2px 10px rgba(0,0,0,0.12);
    overflow: hidden;
  }
  .brand-block {
    position: absolute;
    top: 162px;
    width: 400px;
    text-align: center;
    color: var(--ink);
  }
  .brand-block--first { left: 46px; }
  .brand-block--second { left: 488px; }
  .skyline-artwork {
    display: block;
    width: 150px;
    height: 166px;
    margin: 0 auto 24px;
    background: linear-gradient(180deg, var(--label) 0%, var(--skyline-tint) 100%);
  }
  .brand-name {
    font-weight: 600;
    font-size: 48px;
    line-height: 1;
    color: var(--signal-red);
    letter-spacing: -0.5px;
  }
  .brand-origin {
    margin-top: 6px;
    font-size: 15px;
    letter-spacing: 1.5px;
    color: var(--ink-soft);
  }
  .brand-variety {
    margin-top: 2px;
    font-size: 22px;
    letter-spacing: 6px;
    color: var(--ink);
  }
  .legal-panel {
    position: absolute;
    top: 70px; right: 40px;
    height: 440px;
    display: flex;
    flex-direction: row-reverse;
    gap: 14px;
    align-items: flex-start;
  }
  .legal-text {
    writing-mode: vertical-rl;
    font-size: 10.5px;
    line-height: 16px;
    color: var(--ink);
    font-weight: 600;
    white-space: nowrap;
  }
  .legal-volume {
    writing-mode: vertical-rl;
    display: flex;
    align-items: center;
    gap: 10px;
    font-weight: 700;
    font-size: 22px;
    color: var(--ink);
  }
  .estimated-sign { font-size: 24px; font-weight: 400; }
</style>
</head>
<body>
  <main class="can-label" aria-label="Dosenetikett RheinPerlwein Secco Bianco 200 ml">
    <section class="brand-block brand-block--first">
      <div class="skyline-artwork" role="img" aria-label="Rote Linienzeichnung einer Kölner Stadtsilhouette"></div>
      <h1 class="brand-name">RheinPerlwein</h1>
      <p class="brand-origin">Original italienischer</p>
      <p class="brand-variety">SECCO BIANCO</p>
    </section>

    <section class="brand-block brand-block--second">
      <div class="skyline-artwork" role="img" aria-label="Rote Linienzeichnung einer Kölner Stadtsilhouette"></div>
      <p class="brand-name" aria-hidden="true">RheinPerlwein</p>
      <p class="brand-origin" aria-hidden="true">Original italienischer</p>
      <p class="brand-variety" aria-hidden="true">SECCO BIANCO</p>
    </section>

    <aside class="legal-panel">
      <div class="legal-volume">
        <svg class="recycle-mark" width="20" height="20" viewBox="0 0 20 20" aria-hidden="true">
          <circle cx="10" cy="10" r="8.5" fill="none" stroke="currentColor" stroke-width="1.5"/>
        </svg>
        <span>200ml</span>
        <span class="estimated-sign">℮</span>
      </div>
      <p class="legal-text">
        Secco Bianco del Veneto IGT. Pfandfrei. Weißer Perlwein<br>
        mit zugesetzter Kohlensäure. Enthält Sulfite. Bitte stets gut gekühlt genießen.<br>
        Abgefüllt für Musterfirma GmbH. Verpackt von D-RP100200 in D-56000 Musterstadt.<br>
        Beispielweg 12 / D-50000 Köln / Fon. 0221-1234567 / www.dosenwerk-beispiel.de
      </p>
    </aside>
  </main>
</body>
</html>
```